Wired Earphone Creative Packaging Design

We would like a creative window box style packaging design for our wired earphone

Size: 6” x 3.5” x 1.5” (enclosed die-cut drawing)
Material: E Flute Paper box
Type: Window Box style
Design features we prefer: friendly, playful, creative, trendy, unique, High tech.
Competitors: Enclosed
Requirement:AI file is preferred

Enclosed are product pictures, marketing materials and competitor designs for your reference.

Any further questions, please feel free to ask.
Updates

So designers get more time to design

Target Market(s)

13-40 Year Olds

Industry/Entity Type

Audio

Colors

Designer to choose colors to be used in the design.

Requirements
Must have
• Window, selling point, creative

```html
<!DOCTYPE html>
<html lang="en">
<head>
<meta charset="utf-8">
<title>Stereo In-Ear Earphones – Window Box Dieline</title>
<link rel="stylesheet" href="https://fonts.googleapis.com/css2?family=Montserrat:wght@600;700;800&display=swap">
<style>
  :root {
    --board-yellow: #fff200;
    --cut-line: #1a1a1a;
    --fold-line: #3a5bd9;
    --window-white: #ffffff;
    --ink: #161616;
    --product-white: #f1f1f1;
    --product-grey: #cfcfcf;
    --product-orange: #f6b233;
  }
  html, body {
    margin: 0;
    padding: 0;
    width: 1200px;
    height: 1200px;
    overflow: hidden;
    background: var(--board-yellow);
  }
  .dieline {
    display: block;
    width: 1200px;
    height: 1200px;
    font-family: "Montserrat", sans-serif;
  }
  .cut { fill: none; stroke: var(--cut-line); stroke-width: 1; }
  .fold { fill: none; stroke: var(--fold-line); stroke-width: 1; stroke-dasharray: 4 3; }
  .window { fill: var(--window-white); stroke: var(--cut-line); stroke-width: 1; }
  .spec-text { fill: var(--ink); font-weight: 700; font-size: 11.5px; text-anchor: middle; }
  .headline { fill: var(--ink); font-weight: 800; }
  .model-badge { fill: var(--ink); }
  .model-text { fill: var(--board-yellow); font-weight: 700; }
  .features-title { fill: var(--ink); font-weight: 800; font-size: 22px; }
  .features-line { fill: var(--ink); font-weight: 700; font-size: 13.5px; }
</style>
</head>
<body>
<svg class="dieline" viewBox="0 0 1200 1200" xmlns="http://www.w3.org/2000/svg">
  <defs>
    <linearGradient id="earbud-tone" x1="0" y1="0" x2="1" y2="1">
      <stop offset="0" stop-color="#f6b233"/>
      <stop offset="0.35" stop-color="#f4f4f4"/>
      <stop offset="1" stop-color="#3a3a3a"/>
    </linearGradient>
    <linearGradient id="remote-tone" x1="0" y1="0" x2="0" y2="1">
      <stop offset="0" stop-color="#f2f2f2"/>
      <stop offset="0.6" stop-color="#dcdcdc"/>
      <stop offset="1" stop-color="#e2b630"/>
    </linearGradient>
  </defs>

  <!-- Product imagery -->
  <g class="product-art">
    <rect role="img" aria-label="White earbud with orange rim and black ear tip" x="578" y="94" width="112" height="82" rx="38" fill="url(#earbud-tone)" transform="rotate(-12 634 135)"/>
    <rect role="img" aria-label="In-line remote with yellow buttons" x="820" y="175" width="110" height="48" rx="12" fill="url(#remote-tone)" transform="rotate(-28 875 199)"/>
    <rect role="img" aria-label="White earbud with orange rim and black ear tip" x="430" y="270" width="120" height="84" rx="38" fill="url(#earbud-tone)" transform="rotate(-14 490 312)"/>
    <path d="M478 350 Q490 400 524 430" fill="none" stroke="#ffffff" stroke-width="5"/>
    <rect role="img" aria-label="White earbud with orange rim and black ear tip" x="1000" y="262" width="128" height="100" rx="40" fill="url(#earbud-tone)" transform="rotate(24 1064 312)"/>
    <path d="M990 380 Q1000 345 1040 340" fill="none" stroke="#ffffff" stroke-width="5"/>
    <path d="M680 796 Q640 900 700 925 Q780 950 870 900" fill="none" stroke="#ffffff" stroke-width="6"/>
    <path d="M1130 800 Q1170 780 1200 760" fill="none" stroke="#ffffff" stroke-width="5"/>
    <rect role="img" aria-label="In-line remote controller with yellow side buttons" x="860" y="800" width="290" height="92" rx="14" fill="url(#remote-tone)" transform="rotate(-15 1005 846)"/>
  </g>

  <!-- Top flaps -->
  <path class="cut" d="M32 244 V91 H403 V244"/>
  <rect class="cut" x="108" y="157" width="220" height="16" rx="8"/>
  <path class="cut" d="M94 254 V243 H342 V254"/>
  <path class="cut" d="M408 244 L416 236 V104 Q416 94 426 94 H476 V154 Q476 164 488 164 Q498 164 498 154 V94 H550 Q560 94 560 104 V236 L570 244"/>
  <path class="cut" d="M571 244 V85 H636 V40 Q636 16 660 16 H858 Q882 16 882 40 V85 H946 V244"/>
  <path class="fold" d="M636 85 H882"/>
  <rect class="cut" x="648" y="154" width="221" height="17" rx="8.5"/>
  <path class="cut" d="M948 244 L956 236 V104 Q956 94 966 94 H1020 V154 Q1020 164 1030 164 Q1040 164 1040 154 V94 H1090 Q1100 94 1100 104 V236 L1110 244"/>

  <!-- Body panels -->
  <path class="cut" d="M29 244 V878 H410"/>
  <path class="cut" d="M29 244 H94"/>
  <path class="cut" d="M342 244 H408"/>
  <path class="cut" d="M1110 244 L1194 258 V864 L1110 878"/>
  <path class="fold" d="M408 244 V878 M570 244 V878 M948 244 V878 M1110 244 V878"/>
  <path class="fold" d="M408 244 H1110 M408 878 H1110"/>

  <!-- Bottom flaps -->
  <path class="cut" d="M410 878 L428 1030 H560 V886 L570 878"/>
  <path class="cut" d="M571 878 V1043 H608 V1036 H908 V1043 H946 V878"/>
  <path class="fold" d="M608 1040 H908"/>
  <path class="cut" d="M574 1043 V1080 Q574 1106 600 1106 H916 Q942 1106 942 1080 V1043"/>
  <path class="cut" d="M948 878 L956 886 V1030 H1090 L1106 878"/>

  <!-- Window -->
  <rect class="window" x="526" y="328" width="464" height="468" rx="16"/>

  <!-- Back panel copy -->
  <g class="back-panel">
    <text class="spec-text" x="218" y="285">Earbuds, Controller, Jack, 4 Customizable caps</text>
    <text class="spec-text" x="218" y="314">Contents</text>
    <text class="spec-text" x="218" y="328">2 Pairs of Switchable Caps</text>
    <text class="spec-text" x="218" y="342">3 Pairs of Silicone Ear tips</text>
    <text class="spec-text" x="218" y="357">User Manual</text>
    <text class="spec-text" x="218" y="386">Specification:</text>
    <text class="spec-text" x="218" y="415">Frequency Response: 20-20KHz</text>
    <text class="spec-text" x="218" y="429">Sensitivity: 105±3dB</text>
    <text class="spec-text" x="218" y="444">THD: &lt;3%</text>
    <text class="spec-text" x="218" y="458">Cord Length: 3.6ft</text>
  </g>

  <!-- Side panel features -->
  <g class="side-panel" transform="translate(0 0)">
    <text class="features-title" transform="translate(456 861) rotate(-90)">Features:</text>
    <text class="features-line" transform="translate(475 861) rotate(-90)">Customizable earbuds | In Line Mic | Silicone Gel Ear tips</text>
    <text class="features-line" transform="translate(493 861) rotate(-90)">3.5mm Jack | Ergonomic Design</text>
  </g>

  <!-- Front panel title -->
  <g class="front-panel">
    <text class="headline" x="585" y="272" font-size="23">CUSTOMIZABLE STEREO</text>
    <text class="headline" x="585" y="300" font-size="23">IN- EAR EARPHONES</text>
    <rect class="model-badge" x="586" y="305" width="132" height="14"/>
    <text class="model-text" x="590" y="316" font-size="11">Model Number: SC-1</text>
  </g>

  <!-- Top flap title -->
  <g class="lid-panel">
    <text class="headline" x="714" y="108" font-size="17">CUSTOMIZABLE STEREO</text>
    <text class="headline" x="714" y="128" font-size="17">IN- EAR EARPHONES</text>
    <rect class="model-badge" x="716" y="133" width="100" height="10"/>
    <text class="model-text" x="719" y="141" font-size="8">Model Number: SC-1</text>
  </g>
</svg>
</body>
</html>
```